Business Card Design Project

Corvexa logo will be provided after
Front

Bram Oskarsen- Construction Manager

Ph: (61) 07 53182907
boskarsen@corvexa.com.au
PO Box 83 Kelbarra 4529

Back
Corvexa
EPCM

Oil - Gas - Mining

Industry/Entity Type

Business

Font styles to use
Sans Serif

Colors
faa54b

Requirements
Must have
• White Back Ground

```html
<!DOCTYPE html>
<html lang="en">
<head>
<meta charset="utf-8">
<title>Corvexa Business Card</title>
<link href="https://fonts.googleapis.com/css2?family=Open+Sans:ital,wght@0,400;0,600;0,700;0,800;1,600&display=swap" rel="stylesheet">
<style>
  :root {
    --orange: #faa54b;
    --orange-deep: #f7941d;
    --ink: #1e1e1e;
    --grey: #8f8f8f;
    --grey-light: #c4c4c4;
    --paper: #ffffff;
    --backdrop: #e4e4e4;
  }
  * { box-sizing: border-box; margin: 0; padding: 0; }
  html, body { width: 1200px; height: 676px; overflow: hidden; }
  body {
    background: var(--backdrop);
    font-family: "Open Sans", Arial, sans-serif;
    color: var(--ink);
    position: relative;
  }
  .card {
    position: absolute;
    top: 188px;
    width: 525px;
    height: 300px;
    background: var(--paper);
    box-shadow: 0 6px 18px rgba(0,0,0,0.18);
    overflow: hidden;
  }
  .card--back { left: 50px; }
  .card--front { left: 625px; }

  .wordmark {
    display: flex;
    align-items: center;
    gap: 10px;
    font-weight: 800;
    letter-spacing: 3px;
    color: var(--ink);
    text-transform: uppercase;
    line-height: 1;
  }
  .wordmark__dot {
    border-radius: 50%;
    background: var(--orange-deep);
    flex: none;
  }

  /* back */
  .entity-tag {
    position: absolute;
    top: 22px; left: 26px;
    font-size: 13px;
    font-weight: 600;
    font-style: italic;
    color: var(--orange-deep);
  }
  .card--back .wordmark {
    position: absolute;
    top: 108px; left: 0; right: 0;
    justify-content: center;
    font-size: 50px;
  }
  .card--back .wordmark__dot { width: 22px; height: 22px; }
  .sectors {
    position: absolute;
    right: 0; bottom: 22px;
    display: flex;
    gap: 3px;
    list-style: none;
  }
  .sectors__item {
    background: var(--orange-deep);
    color: var(--paper);
    font-size: 15px;
    font-weight: 600;
    padding: 3px 10px;
  }

  /* front */
  .card--front .wordmark {
    position: absolute;
    top: 46px; left: 30px;
    font-size: 34px;
  }
  .card--front .wordmark__dot { width: 16px; height: 16px; }
  .identity {
    position: absolute;
    right: 40px; top: 98px;
    text-align: right;
  }
  .identity__name {
    font-size: 20px;
    font-weight: 400;
    color: var(--orange-deep);
    line-height: 1.2;
  }
  .identity__role {
    font-size: 13px;
    color: var(--ink);
    line-height: 1.4;
  }
  .rule {
    position: absolute;
    left: 0; top: 160px;
    display: block;
  }
  .contacts {
    position: absolute;
    left: 30px; top: 190px;
    list-style: none;
    font-size: 12px;
  }
  .contacts li { display: flex; align-items: center; gap: 8px; margin-bottom: 6px; }
  .address {
    position: absolute;
    right: 40px; top: 206px;
    display: flex; align-items: center; gap: 6px;
    font-size: 13px;
  }
  .icon { width: 11px; height: 11px; fill: var(--orange-deep); flex: none; }
  .icon--dark { fill: var(--ink); }
</style>
</head>
<body>

<section class="card card--back" aria-label="Card back">
  <p class="entity-tag">Corvexa | EPCM</p>
  <div class="wordmark"><span class="wordmark__dot"></span>Corvexa</div>
  <ul class="sectors">
    <li class="sectors__item">Oil</li>
    <li class="sectors__item">Gas</li>
    <li class="sectors__item">Mining</li>
  </ul>
</section>

<section class="card card--front" aria-label="Card front">
  <div class="wordmark"><span class="wordmark__dot"></span>Corvexa</div>

  <div class="identity">
    <p class="identity__name">Bram Oskarsen</p>
    <p class="identity__role">Construction Manager</p>
  </div>

  <svg class="rule" width="525" height="8" viewBox="0 0 525 8" aria-hidden="true">
    <rect x="0" y="1" width="300" height="4" fill="var(--orange-deep)"/>
    <rect x="300" y="1" width="90" height="4" fill="var(--grey)"/>
    <rect x="390" y="1" width="55" height="4" fill="var(--grey-light)"/>
    <rect x="445" y="0" width="60" height="6" fill="var(--ink)"/>
  </svg>

  <ul class="contacts">
    <li>
      <svg class="icon" viewBox="0 0 24 24"><path d="M6.6 10.8a15 15 0 0 0 6.6 6.6l2.2-2.2c.3-.3.7-.4 1-.2 1.1.4 2.3.6 3.6.6.6 0 1 .4 1 1V20c0 .6-.4 1-1 1C10.6 21 3 13.4 3 4c0-.6.4-1 1-1h3.5c.6 0 1 .4 1 1 0 1.3.2 2.5.6 3.6.1.3 0 .7-.2 1z"/></svg>
      (61) 07 53182907
    </li>
    <li>
      <svg class="icon" viewBox="0 0 24 24"><path d="M2 5h20v14H2zM4 7v.5l8 5 8-5V7zm0 2.8V17h16V9.8l-8 5z"/></svg>
      boskarsen@corvexa.com.au
    </li>
  </ul>

  <p class="address">
    PO Box 83 Kelbarra 4529
    <svg class="icon icon--dark" viewBox="0 0 24 24"><path d="M12 2a7 7 0 0 0-7 7c0 5.3 7 13 7 13s7-7.7 7-13a7 7 0 0 0-7-7zm0 9.5A2.5 2.5 0 1 1 12 6.5a2.5 2.5 0 0 1 0 5z"/></svg>
  </p>
</section>

</body>
</html>
```